Single Webpage Custom Design

We need a single webpage design (no coding) that uses our color and design scheme (http://awareness.morvantshield.com/).
We attached a draft that outlines the structure and content of what the page should look like.
As shown in the draft we need the following sections (in that order):
- Graphic with Text & Logo on top
- Product Explanation
- Customer Logos
- Success Stories with logo and citation each
- Contact form
- Footer

```html
<!DOCTYPE html>
<html lang="de">
<head>
<meta charset="utf-8">
<title>Morvant – Human Firewall</title>
<link rel="stylesheet" href="https://fonts.googleapis.com/css2?family=Montserrat:wght@400;600;700;800&family=Open+Sans:wght@400;600;700&display=swap">
<style>
:root{
  --teal:#1db5c1;
  --teal-dark:#169aa5;
  --teal-light:#5fd0d8;
  --orange:#f7901e;
  --orange-dark:#e67a0a;
  --ink:#2d3a40;
  --muted:#6b7780;
  --line:#dfe6ea;
  --white:#ffffff;
  --soft:#f3f7f8;
}
*{box-sizing:border-box;margin:0;padding:0}
html,body{width:1200px;height:4776px;overflow:hidden}
body{font-family:"Open Sans",Arial,sans-serif;color:var(--ink);background:var(--white);position:relative}
h1,h2,h3,h4,.heading{font-family:"Montserrat",Arial,sans-serif}

/* HERO */
.hero{position:absolute;left:0;top:0;width:1200px;height:860px;background:linear-gradient(180deg,#25bfca 0%,#1aaeb9 100%);overflow:hidden}
.hero-photo{position:absolute;left:640px;top:0;width:560px;height:860px;background:radial-gradient(ellipse at 55% 35%,#b9876a 0%,#8c5a45 30%,#3d6f78 62%,#1aaeb9 90%)}
.nav{position:absolute;left:0;top:0;width:1200px;height:90px;display:flex;align-items:center;justify-content:space-between;padding:0 100px 0 108px;z-index:3}
.brand{display:flex;align-items:center;gap:12px;font-family:"Montserrat",sans-serif;font-weight:800;font-size:30px;color:var(--white)}
.brand-dot{width:34px;height:34px;border-radius:50%;background:var(--orange)}
.menu{display:flex;gap:14px;list-style:none}
.menu li{font-family:"Montserrat",sans-serif;font-weight:600;font-size:15px;color:var(--white);padding:10px 16px;border-radius:4px}
.menu li.active{background:var(--orange)}
.hero-title{position:absolute;left:112px;top:132px;font-weight:800;font-size:50px;color:var(--white);letter-spacing:1px;z-index:2}
.hero-sub{position:absolute;left:112px;top:206px;width:420px;font-size:16px;line-height:24px;color:var(--white);z-index:2}
.chart{position:absolute;left:120px;top:320px;z-index:2}
.benefits{position:absolute;left:354px;top:322px;list-style:none;z-index:2}
.benefits li{display:flex;align-items:center;gap:12px;color:var(--white);font-size:15px;font-weight:600;margin-bottom:16px}
.benefits li::before{content:"";width:10px;height:10px;background:var(--white);border-radius:50%}

/* AWARDS */
.award{position:absolute;background:linear-gradient(180deg,#32c7d1,#18a8b4);color:var(--white);border:6px solid var(--white);box-shadow:0 8px 20px rgba(0,0,0,.15);text-align:center;padding:30px 26px;font-size:15px;line-height:22px;font-weight:600;z-index:4}
.award.center{background:linear-gradient(180deg,#fb9a2a,#ee7e10)}
.award svg{display:block;margin:0 auto 16px}

/* HOW */
.section-title{position:absolute;left:0;width:1200px;text-align:center;font-weight:800;font-size:36px;color:var(--ink);letter-spacing:1px}
.band-teal{position:absolute;left:0;width:1200px;background:linear-gradient(180deg,#25bfca,#1ab0bb)}
.step{position:absolute;top:1320px;width:312px;height:520px;background:var(--white);box-shadow:0 6px 22px rgba(0,0,0,.12);padding:22px 26px;text-align:center;z-index:2}
.step-badge{width:92px;height:92px;margin:0 auto 14px;border:3px solid var(--orange);border-radius:50%;display:flex;flex-direction:column;align-items:center;justify-content:center;font-family:"Montserrat",sans-serif;color:var(--orange)}
.step-badge small{font-size:12px;font-weight:700}
.step-badge b{font-size:30px;font-weight:800;line-height:30px}
.step h3{font-size:19px;font-weight:800;color:var(--teal);margin-bottom:10px}
.step.mid h3{color:var(--orange)}
.step h4{font-size:15px;font-weight:700;margin-bottom:14px}
.step p{font-size:12px;line-height:18px;color:var(--muted);margin-bottom:16px}
.step-point{display:flex;gap:14px;text-align:left;font-size:12px;line-height:17px;color:var(--muted);margin-bottom:14px;padding-top:12px;border-top:1px solid var(--line)}
.step-point i{flex:0 0 34px;height:34px;border:2px solid var(--teal);border-radius:6px}
.step.mid .step-point i{border-color:var(--orange)}

.custom-title{position:absolute;top:1924px;left:0;width:1200px;text-align:center;font-size:34px;font-weight:800;color:var(--white)}
.custom-text{position:absolute;top:1994px;left:260px;width:680px;text-align:center;color:var(--white);font-size:13px;line-height:22px}
.example{position:absolute;top:2140px;width:420px;height:220px;background:var(--white);box-shadow:0 6px 18px rgba(0,0,0,.15);display:flex;gap:18px;padding:16px}
.screen{flex:0 0 230px;height:188px;background:linear-gradient(160deg,#e9eef1,#c9d6dc)}
.example h4{font-size:15px;color:var(--teal);margin:14px 0 10px}
.example p{font-size:12px;line-height:18px;color:var(--muted)}

/* CLIENTS */
.clients-title{position:absolute;top:2510px;left:0;width:1200px;text-align:center;font-weight:800;font-size:34px;line-height:48px;color:var(--ink)}
.clients-title em{font-style:normal;color:var(--orange)}
.logo-box{position:absolute;width:130px;height:108px;background:var(--white);box-shadow:0 3px 14px rgba(0,0,0,.12);display:flex;align-items:center;justify-content:center;text-align:center;font-family:"Open Sans",sans-serif;font-weight:700;font-size:17px;color:var(--ink)}

/* STORIES */
.stories{position:absolute;left:0;top:3040px;width:1200px;height:480px;background:linear-gradient(180deg,#fa9626,#ef800f)}
.stories h2{position:absolute;top:56px;left:0;width:1200px;text-align:center;color:var(--white);font-size:36px;font-weight:800}
.story{position:absolute;top:150px;width:460px;color:var(--white)}
.story-brand{font-family:"Open Sans",sans-serif;font-weight:700;font-size:34px;color:var(--white);height:54px;display:flex;align-items:center;gap:12px}
.story-brand span{width:34px;height:34px;border-radius:50%;background:var(--white)}
.story q{display:block;font-style:italic;font-size:16px;line-height:26px;margin-top:18px}
.btn-ghost{position:absolute;width:150px;height:44px;border:2px solid var(--white);border-radius:22px;color:var(--white);font-family:"Montserrat",sans-serif;font-weight:700;font-size:13px;display:flex;align-items:center;justify-content:center}

/* CONTACT */
.contact-form{position:absolute;left:256px;top:3690px;width:690px}
.field{position:absolute;height:50px;border:1px solid var(--line);background:var(--white);font-size:13px;color:#9aa4aa;padding:15px 14px}
.submit{position:absolute;left:282px;top:384px;width:130px;height:46px;background:var(--orange);color:var(--white);border-radius:23px;font-family:"Montserrat",sans-serif;font-weight:700;font-size:14px;display:flex;align-items:center;justify-content:center}

/* FOOTER */
.footer{position:absolute;left:0;top:4160px;width:1200px;height:616px;background:linear-gradient(180deg,#20b9c4,#17a5b0);color:var(--white)}
.fcol{position:absolute;top:56px}
.fcol h4{font-size:26px;font-weight:800;margin-bottom:20px}
.fcol p,.fcol li{font-size:12px;line-height:19px}
.fcol b{font-size:13px;display:block;margin-top:8px}
.fcol ul{list-style:none}
.fcol li{display:flex;align-items:center;gap:10px;margin-bottom:9px}
.input-w{width:150px;height:36px;background:var(--white);border-radius:3px;font-size:12px;color:var(--muted);padding:9px 10px}
.dot{width:24px;height:24px;border-radius:50%;border:2px solid var(--white)}
.copyright{position:absolute;bottom:28px;left:0;width:1200px;text-align:center;font-size:12px}
</style>
</head>
<body>

<header class="hero">
  <div class="hero-photo" role="img" aria-label="Photo of a confident woman in a superhero cape standing in front of a brick wall"></div>
  <nav class="nav">
    <div class="brand"><span class="brand-dot"></span>Morvant</div>
    <ul class="menu">
      <li class="active">HOME</li><li>SOLUTION</li><li>PRICING</li><li>ABOUT</li><li>CONTACT US</li>
    </ul>
  </nav>
  <h1 class="hero-title">HUMAN FIREWALL</h1>
  <p class="hero-sub">Mittels Cyber Awareness Schulungen das Risiko von Attacken innerhalb von 12 Monaten messbar um 90% senken</p>
  <svg class="chart" width="240" height="460" viewBox="0 0 240 460">
    <rect x="10" y="40" width="40" height="340" fill="var(--orange)"/>
    <g fill="#fdba6e">
      <rect x="66" y="230" width="40" height="150"/>
      <rect x="122" y="290" width="40" height="90"/>
      <rect x="178" y="330" width="40" height="50"/>
    </g>
    <line x1="0" y1="380" x2="232" y2="380" stroke="#ffffff" stroke-width="2"/>
    <g fill="#ffffff" font-family="Open Sans, sans-serif" font-size="11" text-anchor="middle">
      <text x="30" y="400">Initial</text><text x="30" y="414">Training</text>
      <text x="86" y="400">Attack</text><text x="86" y="414">Simulation</text>
      <text x="142" y="400">Security</text><text x="142" y="414">Quizzes</text>
      <text x="198" y="400">Post Quiz</text><text x="198" y="414">Training</text>
    </g>
  </svg>
  <ul class="benefits">
    <li>Geld-Zurück-Garantie</li>
    <li>Individualisierbare Inhalte</li>
    <li>Preiswerte Lösung</li>
    <li>Datenschutzkonform</li>
  </ul>
</header>

<div class="award" style="left:112px;top:880px;width:300px;height:220px">
  <svg width="56" height="56" viewBox="0 0 56 56" fill="none" stroke="#fff" stroke-width="3"><path d="M16 8h24v14a12 12 0 0 1-24 0z"/><path d="M16 12H8v4a8 8 0 0 0 8 8M40 12h8v4a8 8 0 0 1-8 8M28 34v10M18 48h20"/></svg>
  In 2020, Morvant won the Cyber Security Excellence Award for Best "Anti Phishing"
</div>
<div class="award center" style="left:430px;top:740px;width:340px;height:400px;padding-top:64px">
  <svg width="76" height="76" viewBox="0 0 76 76" fill="none" stroke="#fff" stroke-width="3"><circle cx="38" cy="30" r="20"/><path d="M38 20l3 7 7 1-5 5 1 7-6-3-6 3 1-7-5-5 7-1z"/><path d="M26 46l-6 24 10-5 6 8 2-22M50 46l6 24-10-5-6 8-2-22"/></svg>
  In 2020, Morvant won the Cyber Security Excellence Award for Best "Security Education Platform"
</div>
<div class="award" style="left:788px;top:880px;width:300px;height:220px">
  <svg width="56" height="56" viewBox="0 0 56 56" fill="none" stroke="#fff" stroke-width="3"><circle cx="28" cy="26" r="12"/><path d="M10 14c-4 10 0 22 10 28M46 14c4 10 0 22-10 28M28 38v12"/></svg>
  2020 Gold Winner of the "Cyber Security Education &amp; Platform" category in the Security Product
</div>

<h2 class="section-title" style="top:1214px">HOW DOES IT WORK?</h2>
<div class="band-teal" style="top:1600px;height:860px"></div>

<article class="step" style="left:126px">
  <div class="step-badge"><small>STEP</small><b>01</b></div>
  <h3>SET GOALS &amp; CREATE A PLAN</h3>
  <h4>Understanding Your Goals Will Define Program Scope</h4>
  <p>A well-documented plan will ensure that goals become measurable and your cloud security awareness grows to value.</p>
  <div class="step-point"><i></i><span>Understand your compliance requirements, available resources and budget restrictions.</span></div>
  <div class="step-point"><i></i><span>Define target groups, required languages, and other training constraints.</span></div>
</article>
<article class="step mid" style="left:444px">
  <div class="step-badge"><small>STEP</small><b>02</b></div>
  <h3>ASSESS AWARENESS LEVEL</h3>
  <h4>Use Phishing Simulations Or Assessments To Understand The Current Awareness Level</h4>
  <p>In order to improve user behavior, we recommend measuring the current status through attack simulations or surveys.</p>
  <div class="step-point"><i></i><span>Perform sample phishing simulations with employees from different departments.</span></div>
  <div class="step-point"><i></i><span>Create interactive exams where users can test their knowledge.</span></div>
</article>
<article class="step" style="left:762px">
  <div class="step-badge"><small>STEP</small><b>03</b></div>
  <h3>RUN THE AWARENESS CAMPAIGN</h3>
  <h4>Improve The Security Awareness Level With Tailored Courses. Optimize The Program Over Time.</h4>
  <p>The awareness campaign is an ongoing process and lessons from last year’s testing it has to evolve to future settings.</p>
  <div class="step-point"><i></i><span>Create risk-based awareness trainings for different departments with measure progress.</span></div>
  <div class="step-point"><i></i><span>Analyze the results and adjust the training program. Repeat the steps every time again with tracking.</span></div>
</article>

<h2 class="custom-title">FULLY CUSTOMIZABLE!</h2>
<p class="custom-text">You Might Ask – Why Are The Trainings More Customizable? All Modifiers For Adjusting The Design (Logo/Fonts/Colors) To Your Corporate Look And Feel. It Is Important That Your Employees Recognize The Training As Something They Can Relate To.<br><br>Examples:</p>
<div class="example" style="left:160px">
  <div class="screen" role="img" aria-label="Screenshot of a customized training dashboard"></div>
  <div><h4>From CEO:</h4><p>Add a personal guiding message from your CEO at the start of the course to highlight the importance of the training.</p></div>
</div>
<div class="example" style="left:620px">
  <div class="screen" role="img" aria-label="Screenshot of a company policy training page"></div>
  <div><h4>Do You Know Your Policies?</h4><p>You could ask the user to read and acknowledge your internal policies prior to starting the course.</p></div>
</div>

<h2 class="clients-title">MEHR ALS <em>400</em> KUNDEN<br>VERTRAUEN BEREITS AUF MORVANT</h2>
<div class="logo-box" style="left:110px;top:2690px">Alvera</div>
<div class="logo-box" style="left:312px;top:2690px">Nordwell</div>
<div class="logo-box" style="left:514px;top:2690px;font-size:15px">Kessler Werke</div>
<div class="logo-box" style="left:712px;top:2690px">Veltrasa</div>
<div class="logo-box" style="left:910px;top:2690px">Oxal</div>
<div class="logo-box" style="left:210px;top:2850px">Brauner</div>
<div class="logo-box" style="left:412px;top:2850px">Clarenta</div>
<div class="logo-box" style="left:614px;top:2850px">Vendura</div>
<div class="logo-box" style="left:812px;top:2850px">Bortek</div>

<section class="stories">
  <h2>SUCCESS STORIES</h2>
  <div class="story" style="left:112px">
    <div class="story-brand"><span></span>Skyvarta</div>
    <q>Morvant bietet ein optimales Gesamtpaket, mit dem wir die awareness der unserer mitarbeitenden dauerhaft hochhalten können.</q>
  </div>
  <div class="btn-ghost" style="left:112px;top:376px">READ MORE</div>
  <div class="story" style="left:652px">
    <div class="story-brand"><span></span>Feldmark</div>
    <q>Es ist einfach ein tolles gefühl, wenn man sieht, dass mir mitarbeiter deutlich wachsamer geworden sind.</q>
  </div>
  <div class="btn-ghost" style="left:652px;top:376px">READ MORE</div>
</section>

<h2 class="section-title" style="top:3596px">CONTACT US</h2>
<form class="contact-form" style="height:440px">
  <div class="field" style="left:0;top:0;width:336px">Full Name *</div>
  <div class="field" style="left:354px;top:0;width:336px">Your Email *</div>
  <div class="field" style="left:0;top:70px;width:336px">Phone</div>
  <div class="field" style="left:354px;top:70px;width:336px">Subject *</div>
  <div class="field" style="left:0;top:140px;width:690px">Country –</div>
  <div class="field" style="left:0;top:210px;width:690px;height:150px">Message *</div>
  <div class="submit">SUBMIT</div>
</form>

<footer class="footer">
  <div class="fcol" style="left:112px;width:260px">
    <h4>CONTACTS US</h4>
    <b>EUROPE</b>
    <p>Morvant Shield AG, Lindenweg 12<br>6300 Talberg, Switzerland</p>
    <b>NORTH AMERICA</b>
    <p>Morvant Shield USA, 4820 Harbor Lane<br>Suite 210, Millbrook, TX 70000</p>
    <p style="margin-top:14px">Phone Global: +41 00 000 1010<br>Phone USA: +1 000 000 2020<br>Phone USA Support: +1 000 000 3030<br>Phone Canada: +1 000 000 4040<br>Phone France: +33 0 00 00 50 50<br>Phone UK: +44 00 0000 6060</p>
  </div>
  <div class="fcol" style="left:412px;width:200px">
    <h4>SEARCH</h4>
    <div class="input-w">Search...</div>
    <h4 style="margin-top:22px">CONNECT</h4>
    <ul>
      <li><span class="dot"></span>Community</li>
      <li><span class="dot"></span>News Feed</li>
      <li><span class="dot"></span>Video Channel</li>
      <li><span class="dot"></span>Pro Network</li>
    </ul>
  </div>
  <div class="fcol" style="left:680px;width:200px">
    <h4>INFORMATION</h4>
    <ul>
      <li>› Home</li><li>› Solution</li><li>› Pricing</li><li>› Resources</li><li>› About Us</li><li>› Support Wiki</li><li>› Contact</li><li>› Download Morvant</li><li>› Demo Request</li>
    </ul>
  </div>
  <div class="fcol" style="left:924px;width:180px">
    <h4>LANGUAGE</h4>
    <div class="input-w" style="width:130px">Deutsch ▾</div>
  </div>
  <p class="copyright">© Copyright 2021 All Rights Reserved</p>
</footer>

</body>
</html>
```